Website design for legal tech start up in Switzerland (B2B)

We are for a legal tech start up in Switzerland called MIVA. We have been running since August 2016. This will be our first live website.

We need a website designed and business card design for our start-up in Switzerland. We also need the Web design to be converted into HTML and CSS files.

Function of website:
• To inform potential customers of our services
• Form a key part of our digital marketing and sales footprint.
• Branding

Please find attached logo.

Reason: Looking for more idea's not necessarily set on blue and grey colours only.

Target Market(s)

B2B tech powered legal services.

Industry/Entity Type

Legal

Contact Information for Business Card

Lean and slick design.

Coding

Coded - Design and coding required

Number of Pages Required

5+ page

Requirements
Must have
• VERY LEAN AND CLEAN DESIGN!
• We have received many great standard designs, but we are looking for something more out-of-the box: You can get inspiration from these designs: http://www.plimbergallery.net/websites/clean/
• Thanks!!
• Easy content management system
• Well structured coding for additional development
• Responsive webpage for all types of devices
• SEO optimized
• Tabs (Home, services, team, careers, blog, contact us)
• Colour scheme complementary to logo
Nice to have
• Look and Design - Approachable, High-tech, Modern
• Easy to add chat bot capability in future
Should not have
• Too busy/ too much clutter
• Not take to long to load

```html
<!DOCTYPE html>
<html lang="en">
<head>
<meta charset="utf-8">
<title>MIVA — Legal Tech for Business</title>
<link href="https://fonts.googleapis.com/css2?family=Lato:wght@300;400;700;900&family=Lora:wght@700&family=Cinzel&display=swap" rel="stylesheet">
<style>
:root{
  --navy:#1f3354;
  --navy-dark:#18294a;
  --blue:#0d4a8a;
  --orange:#ee4d1f;
  --gold:#c9a46a;
  --text:#5f6770;
  --muted:#9aa0a6;
  --white:#fff;
  --badge:#d8dde4;
}
*{margin:0;padding:0;box-sizing:border-box}
html,body{width:1200px;height:1200px;overflow:hidden;background:var(--white);font-family:'Lato',sans-serif}
.page{position:relative;width:1200px;height:1200px}
.abs{position:absolute}
.topbar .call{left:172px;top:6px;font-size:14px;color:var(--muted);font-weight:300}
.topbar .call b{color:var(--blue);font-weight:400}
.toplinks{right:138px;top:9px;display:flex;gap:18px;font-size:10px;color:var(--orange);text-transform:uppercase}
.hero{left:59px;top:29px;width:1080px;height:560px;background:linear-gradient(120deg,#26395a 0%,var(--navy) 45%,var(--navy-dark) 100%)}
.logo-box{left:163px;top:29px;width:174px;height:70px;background:var(--white);display:flex;align-items:center;justify-content:center;font-size:40px;font-weight:700;color:#444c56;letter-spacing:2px}
.nav{right:137px;top:58px;display:flex;gap:34px;font-size:14px;font-weight:700;color:var(--white)}
.cta-label{left:620px;width:360px;top:200px;text-align:center;font-size:35px;font-weight:900;color:var(--gold)}
.cta-phone{left:560px;width:480px;top:250px;text-align:center;font-family:'Lora',serif;font-size:40px;font-weight:700;color:var(--white);white-space:nowrap}
.cta-btn{left:669px;top:332px;width:268px;height:34px;border:1px solid var(--orange);color:var(--orange);font-size:14px;font-weight:700;display:flex;align-items:center;justify-content:center}
.features{left:163px;top:459px;width:900px;height:130px;background:var(--white)}
.feature{position:absolute;width:270px;text-align:center}
.feature .icon{position:absolute;left:113px;width:44px;height:44px;border-radius:50%;background:var(--orange);display:flex;align-items:center;justify-content:center}
.feature p{font-size:16px;line-height:21px;color:var(--text)}
.feature a{display:block;font-size:12px;color:var(--blue);text-decoration:none}
.photo{left:143px;top:646px;width:288px;height:312px;background:linear-gradient(180deg,#0d4a8a 0%,#1a5797 55%,#e9edf2 56%,#f4f6f8 100%)}
.firm-name{left:143px;width:288px;top:966px;text-align:center;font-size:22px;color:#4d6a8a}
.badge{background:var(--badge);border-radius:4px}
.firm-tag{left:143px;width:300px;top:1082px;text-align:center;font-family:'Cinzel',serif;font-size:19px;line-height:26px;color:var(--blue)}
.col h2{font-size:16px;font-weight:700;color:var(--blue);line-height:26px}
.col p{margin-top:16px;font-size:12px;line-height:25.6px;color:var(--text);font-weight:300}
.col .more{display:block;margin-top:6px;font-size:10.5px;color:var(--orange)}
</style>
</head>
<body>
<div class="page">
  <div class="topbar">
    <div class="abs call">Call us: <b>+41 44 555 01 28</b></div>
    <div class="abs toplinks"><span>Request a free consultation →</span><span>Videos</span><span>FAQ's</span><span>Blog</span></div>
  </div>

  <section class="abs hero" role="img" aria-label="Dark blue city skyline background"></section>
  <div class="abs logo-box">MIVA</div>
  <nav class="abs nav"><span>HOME</span><span>SERVICES</span><span>TEAM</span><span>CAREERS</span><span>CONTACT US</span></nav>
  <div class="abs cta-label">CALL US:</div>
  <div class="abs cta-phone">+41 44 555 01 28</div>
  <div class="abs cta-btn">REQUEST A FREE CONSULTATION →</div>

  <div class="abs features">
    <div class="feature" style="left:22px;top:0">
      <div class="icon" style="top:-22px"><svg width="22" height="22" viewBox="0 0 24 24" fill="none" stroke="#fff" stroke-width="1.6"><circle cx="10" cy="8" r="4"/><path d="M3 20c0-4 3-6 7-6s7 2 7 6z"/><path d="M15 5a4 4 0 0 1 0 7M18 14c2 1 3 3 3 6"/></svg></div>
      <p style="margin-top:36px">Lean legal teams, backed<br>by smart automation</p>
      <a style="margin-top:14px">OUR SERVICES →</a>
    </div>
    <div class="feature" style="left:313px;top:0">
      <div class="icon" style="top:-22px"><svg width="22" height="22" viewBox="0 0 24 24" fill="none" stroke="#fff" stroke-width="1.6"><path d="M7 3h10v5a5 5 0 0 1-10 0z"/><path d="M7 5H3c0 3 2 5 4 5M17 5h4c0 3-2 5-4 5M12 13v4M8 21h8M9 17h6"/></svg></div>
      <p style="margin-top:31px">Contracts reviewed<br>in hours, not weeks</p>
      <a style="margin-top:19px">HOW IT WORKS →</a>
    </div>
    <div class="feature" style="left:622px;top:0">
      <div class="icon" style="top:-19px"><svg width="22" height="22" viewBox="0 0 24 24" fill="none" stroke="#fff" stroke-width="1.6"><circle cx="12" cy="8" r="4.5"/><path d="M3 21c0-5 4-7 9-7s9 2 9 7z"/></svg></div>
      <p style="margin-top:41px">Swiss lawyers and engineers<br>on one team</p>
      <a style="margin-top:9px">MEET THE TEAM →</a>
    </div>
  </div>

  <div class="abs photo" role="img" aria-label="Portrait of the founding lawyer"></div>
  <div class="abs firm-name">MIVA</div>
  <div class="abs badge" style="left:160px;top:1016px;width:116px;height:44px;border-radius:22px 4px 4px 22px"></div>
  <div class="abs badge" style="left:316px;top:1008px;width:104px;height:52px"></div>
  <div class="abs firm-tag">Zurich Legal Tech<br>for Business</div>

  <div class="abs badge" style="left:453px;top:681px;width:50px;height:80px"></div>
  <div class="abs badge" style="left:513px;top:688px;width:50px;height:60px;background:#eceff3"></div>
  <div class="abs badge" style="left:586px;top:682px;width:135px;height:78px"></div>
  <div class="abs badge" style="left:774px;top:674px;width:124px;height:94px;border-radius:50%"></div>
  <div class="abs badge" style="left:924px;top:688px;width:80px;height:40px"></div>

  <div class="abs col" style="left:450px;top:782px;width:292px">
    <h2>Legal Work Built Like Software, Checked by Swiss Lawyers</h2>
    <p style="text-align:justify">MIVA combines legal engineering with experienced Swiss counsel. We turn repetitive legal work such as contract review, NDAs, employment terms and data protection checks into clear, automated workflows. Your team uploads a document, our platform flags the risks, and a qualified lawyer confirms every result before it reaches you. The outcome is faster turnaround, fixed and transparent pricing, and a full audit trail for every matter. No billable hours and no surprises, just dependable answers when your business needs them...</p>
    <span class="more">READ MORE →</span>
  </div>
  <div class="abs col" style="left:767px;top:782px;width:290px">
    <h2>MIVA Keeps Your Company Compliant</h2>
    <p style="margin-top:42px">Regulation in Switzerland and the EU changes constantly, and keeping up is a full-time job. MIVA monitors the rules that matter to your sector and translates them into practical checklists for your teams. Our dashboard shows open obligations, upcoming deadlines and the status of every contract in one place. Start-ups use MIVA to set up their first legal framework quickly, while growing companies rely on it to scale compliance without hiring a large in-house department. Every plan includes direct access to a Swiss lawyer, clear reporting for management, and secure hosting in Switzerland. Get in touch for a short demo and see how your legal work can become simpler...</p>
    <span class="more" style="margin-top:2px">READ MORE →</span>
  </div>
</div>
</body>
</html>
```